Webdesign für Getränkelogistik & Full-Service-Partner bei Events
Zielgruppe
Getränkelogistiker und Full-Service-Partner bei Events
Zielgruppe: Getränke-EinzelHändler; Veranstalter von Events und privaten Feiern
Aufgabenstellung
- soll „Frische“ und „Moderne“ vermitteln, ohne eine Getränkeart in den Vordergrund zu rücken
- soll von den Farben her gut zum Logo passen (siehe Anlagen)
- Slider wäre wünschenswert
- Slogan 'Wir freuen uns auf Sie!'

```html
<!DOCTYPE html>
<html lang="de">
<head>
<meta charset="utf-8">
<title>Getränke Halden GmbH</title>
<link href="https://fonts.googleapis.com/css2?family=Open+Sans:wght@400;600;700&family=Playfair+Display:wght@700;900&display=swap" rel="stylesheet">
<style>
:root{
  --green:#22675e;
  --green-dark:#1c5a52;
  --yellow:#f9c300;
  --yellow-deep:#f2b800;
  --text:#3a3a3a;
  --rule:#c9c9c9;
  --white:#ffffff;
}
*{margin:0;padding:0;box-sizing:border-box}
html,body{width:1146px;height:1200px;overflow:hidden}
body{position:relative;font-family:"Open Sans",Arial,sans-serif;color:var(--text);
  background:linear-gradient(180deg,#fff 0,#fff 810px,#f1f1f1 900px,#e6e6e6 1030px,var(--yellow) 1040px,#f7cf1c 1120px,var(--yellow-deep) 1200px)}
.abs{position:absolute}
.brand{left:0;width:1146px;top:28px;display:flex;justify-content:center;align-items:center;gap:8px}
.brand-dot{width:22px;height:22px;border-radius:50%;background:var(--yellow)}
.brand-name{font-weight:700;font-size:22px;color:var(--green)}
.nav{left:222px;width:703px;top:90px;height:47px;border-top:1px solid var(--rule);border-bottom:1px solid var(--rule);
  display:flex;justify-content:center;align-items:center;gap:28px;font-size:11px;color:#555}
.nav .active{color:var(--green);font-weight:700}
.hero{left:140px;top:154px;width:865px;height:421px}
.slogan{left:220px;top:274px;font-family:"Playfair Display",Georgia,serif;font-weight:700;font-size:39px;line-height:44px;color:var(--yellow)}
.thumbs{left:222px;top:516px;display:flex;gap:6px}
.thumb{width:42px;height:42px}
.thumb.current{outline:2px solid var(--yellow);outline-offset:-2px}
.hotline{left:994px;top:172px;width:152px;height:58px;background:var(--yellow);padding:8px 0 0 11px}
.hotline small{display:block;font-size:11px;color:#333}
.hotline strong{display:block;font-size:20px;font-weight:700;color:var(--green);line-height:24px}
.service{top:644px;width:163px}
.service-label{font-size:10px;font-weight:700;color:var(--yellow);letter-spacing:.2px}
.service-rule{width:30px;height:1px;background:#bbb;margin:11px 0 14px}
.service-title{font-family:"Playfair Display",Georgia,serif;font-weight:700;font-size:22px;color:var(--green);line-height:28px}
.service-text{font-size:10.6px;line-height:16.7px;margin-top:16px;height:80px}
.service-photo{width:162px;height:111px;margin-top:0}
.more{display:block;text-align:right;margin-top:13px;font-size:11.5px;font-weight:700;color:var(--green);text-decoration:underline}
.footer-col{top:1063px;font-size:11px;line-height:21.6px;color:#333}
.footer-col ul{list-style:none}
.icon{position:absolute;left:0}
.footer-rule{left:222px;width:703px;top:1161px;height:1px;background:#555}
.copy{left:0;width:1146px;top:1172px;text-align:center;font-size:11px;color:#333}
</style>
</head>
<body>
<div class="abs brand"><span class="brand-dot"></span><span class="brand-name">Getränke Halden GmbH</span></div>

<nav class="abs nav">
  <span class="active">Home</span><span>Unternehmen</span><span>Team</span><span>Großhandel</span><span>Rund um Ihr Event</span><span>Karriere</span><span>Kontakt</span>
</nav>

<svg class="abs hero" viewBox="0 0 865 421" role="img" aria-label="Slider-Foto: zwei lachende Frauen stoßen mit bunten Getränkeflaschen an">
  <defs>
    <linearGradient id="photoTone" x1="0" y1="0" x2="1" y2="1">
      <stop offset="0" stop-color="#f3eee4"/>
      <stop offset=".35" stop-color="#f2b28a"/>
      <stop offset=".65" stop-color="#e58a6a"/>
      <stop offset="1" stop-color="#6f9fc2"/>
    </linearGradient>
  </defs>
  <rect width="865" height="421" fill="var(--green)"/>
  <path d="M422 0 C330 80 300 160 312 240 C322 320 400 390 470 421 L865 421 L865 0 Z" fill="var(--yellow)"/>
  <path d="M432 0 C342 82 312 162 322 240 C332 318 408 386 482 421 L865 421 L865 0 Z" fill="url(#photoTone)"/>
</svg>

<div class="abs slogan">“Wir freuen<br>uns auf Sie!”</div>

<div class="abs thumbs">
  <div class="thumb current" role="img" aria-label="Vorschau: Frauen mit Getränken" style="background:linear-gradient(135deg,#f4c48a,#e07c6a)"></div>
  <div class="thumb" role="img" aria-label="Vorschau: Partygäste stoßen an" style="background:linear-gradient(135deg,#f38aa0,#b8262e)"></div>
  <div class="thumb" role="img" aria-label="Vorschau: Weingläser" style="background:linear-gradient(135deg,#e8d8c0,#5a1e14)"></div>
  <div class="thumb" role="img" aria-label="Vorschau: Erfrischungsgetränke mit Minze" style="background:linear-gradient(135deg,#8ad0e8,#f2f2d8)"></div>
</div>

<div class="abs hotline"><small>Bestell-Hotline:</small><strong>034512 60420</strong></div>

<section class="abs service" style="left:222px">
  <div class="service-label">SERVICE 01</div><div class="service-rule"></div>
  <h2 class="service-title">Für Ihr Event</h2>
  <p class="service-text">Dies ist ein Typoblindtext. An ihm kann man sehen, ob alle Buchstaben da sind und wie sie aussehen.</p>
  <div class="service-photo" role="img" aria-label="Foto: festlich geschmücktes Eventzelt unter blauem Himmel" style="background:linear-gradient(160deg,#2a3ec0,#8fa6e0 45%,#e9e9ef)"></div>
  <a class="more">weiterlesen</a>
</section>
<section class="abs service" style="left:402px">
  <div class="service-label">SERVICE 02</div><div class="service-rule"></div>
  <h2 class="service-title">Großhandel</h2>
  <p class="service-text">Dies ist ein Typoblindtext. An ihm kann man sehen, ob alle Buchstaben da sind und wie sie aussehen.</p>
  <div class="service-photo" role="img" aria-label="Foto: grüne Lieferlastwagen in einer Reihe" style="background:linear-gradient(180deg,#d9dde0 0,#d9dde0 30%,#1f5a2c 45%,#1a4d26 75%,#6a6a6a)"></div>
  <a class="more">weiterlesen</a>
</section>
<section class="abs service" style="left:581px">
  <div class="service-label">SERVICE 03</div><div class="service-rule"></div>
  <h2 class="service-title">Unternehmen</h2>
  <p class="service-text">Dies ist ein Typoblindtext. An ihm kann man sehen, ob alle Buchstaben da sind und wie sie aussehen.</p>
  <div class="service-photo" role="img" aria-label="Foto: Geschäftsführer am Treppengeländer" style="background:linear-gradient(135deg,#9aa0a0,#e4e6e6 50%,#7b7f80)"></div>
  <a class="more">weiterlesen</a>
</section>
<section class="abs service" style="left:762px">
  <div class="service-label">SERVICE 04</div><div class="service-rule"></div>
  <h2 class="service-title">Team</h2>
  <p class="service-text">Dies ist ein Typoblindtext. An ihm kann man sehen, ob alle Buchstaben da sind und wie sie aussehen.</p>
  <div class="service-photo" role="img" aria-label="Foto: Mitarbeiterteam vor der Lagerhalle" style="background:linear-gradient(180deg,#c8c21a 0,#3a3d38 20%,#6a6e68 60%,#2e4a34)"></div>
  <a class="more">weiterlesen</a>
</section>

<div class="abs footer-col" style="left:222px;padding-left:18px">
  <svg class="icon" style="top:4px" width="13" height="17" viewBox="0 0 13 17"><path d="M6.5 0A6.5 6.5 0 0 0 0 6.5C0 11 6.5 17 6.5 17S13 11 13 6.5A6.5 6.5 0 0 0 6.5 0Z" fill="var(--green)"/><circle cx="6.5" cy="6.5" r="2.4" fill="var(--yellow)"/></svg>
  Getränke Halden GmbH<br>Am Mühlgraben 14<br>09387 Lindenau
</div>
<div class="abs footer-col" style="left:464px;padding-left:23px">
  <svg class="icon" style="top:3px" width="15" height="15" viewBox="0 0 24 24"><path d="M6.6 10.8a15 15 0 0 0 6.6 6.6l2.2-2.2c.3-.3.7-.4 1-.2 1.1.4 2.3.6 3.6.6.6 0 1 .4 1 1V20c0 .6-.4 1-1 1A17 17 0 0 1 3 4c0-.6.4-1 1-1h3.5c.6 0 1 .4 1 1 0 1.3.2 2.5.6 3.6.1.3 0 .7-.2 1Z" fill="var(--green)"/></svg>
  Telefon: +49 34512 60420<br>Telefax: +49 34512 60421<br>
  <svg class="icon" style="top:48px" width="16" height="12" viewBox="0 0 16 12"><rect width="16" height="12" rx="1.5" fill="var(--green)"/><path d="M1 1.5 8 7l7-5.5" stroke="var(--yellow)" stroke-width="1.4" fill="none"/></svg>
  info(at)getraenke-halden.de
</div>
<div class="abs footer-col" style="left:701px;top:1061px">
  <ul><li>• Downloads</li><li>• Kontakt</li><li>• Impressum/Datenschutz</li><li>• AGB</li></ul>
</div>
<div class="abs footer-rule"></div>
<div class="abs copy">© 2020 getraenke-halden.de</div>
</body>
</html>
```